Futuristic but clean CD Cover Design

I need a CD Cover design for my next EP. The music is electronic pop. I am looking for something clean but futuristic with neon colors .Name of band: peopleASponiesName of Album: CeylonI have attached my logo.I have also attached CD covers of the color scheme and clean look I am looking for.Thanks

Industry/Entity Type

Film Production

Requirements
Must have
• A clean future look. The music is electronic pop.

```html
<!DOCTYPE html>
<html lang="en">
<head>
<meta charset="utf-8">
<title>Varmel — lanternSOkites</title>
<link rel="stylesheet" href="https://fonts.googleapis.com/css2?family=Orbitron:wght@800&family=Exo+2:wght@300&display=swap">
<style>
  :root {
    --bg-deep: #1e0b24;
    --neon-pink: #ff33ff;
    --neon-line: #ff4fd8;
    --extrude-blue: #3a22e0;
    --extrude-shadow: #2a1690;
    --band-lilac: #d8a8e6;
  }
  html, body {
    margin: 0;
    padding: 0;
    width: 1200px;
    height: 1200px;
    overflow: hidden;
    background: var(--bg-deep);
  }
  .cover {
    position: relative;
    width: 1200px;
    height: 1200px;
  }
  .cover svg { display: block; }
  .album-title {
    font-family: "Orbitron", "Audiowide", sans-serif;
    font-weight: 800;
    font-size: 196px;
  }
  .band-name {
    font-family: "Exo 2", "Rajdhani", sans-serif;
    font-weight: 300;
    font-size: 84px;
    fill: var(--band-lilac);
  }
</style>
</head>
<body>
<main class="cover">
  <svg width="1200" height="1200" viewBox="0 0 1200 1200" xmlns="http://www.w3.org/2000/svg">
    <defs>
      <linearGradient id="skyTone" x1="0" y1="0" x2="0.3" y2="1">
        <stop offset="0" stop-color="#2c0e34"/>
        <stop offset="0.45" stop-color="#3a1248"/>
        <stop offset="1" stop-color="#2a0f3c"/>
      </linearGradient>
      <radialGradient id="halo" cx="0.5" cy="0.5" r="0.5">
        <stop offset="0" stop-color="#8a1fa0"/>
        <stop offset="0.65" stop-color="#64187a"/>
        <stop offset="1" stop-color="#3a1248" stop-opacity="0"/>
      </radialGradient>
      <linearGradient id="floorTone" x1="0" y1="0" x2="0" y2="1">
        <stop offset="0" stop-color="#0c0a1c" stop-opacity="0"/>
        <stop offset="0.18" stop-color="#0c0a1c"/>
        <stop offset="0.6" stop-color="#1c0c34"/>
        <stop offset="1" stop-color="#2a0c40"/>
      </linearGradient>
      <filter id="glow" x="-10%" y="-200%" width="120%" height="500%">
        <feGaussianBlur stdDeviation="3" result="b"/>
        <feMerge><feMergeNode in="b"/><feMergeNode in="SourceGraphic"/></feMerge>
      </filter>
      <filter id="soft"><feGaussianBlur stdDeviation="30"/></filter>
    </defs>

    <rect class="backdrop" width="1200" height="1200" fill="url(#skyTone)"
          role="img" aria-label="Abstract backdrop of floating violet and blue polygon shards"/>

    <ellipse class="halo" cx="600" cy="650" rx="620" ry="230" fill="url(#halo)" filter="url(#soft)"/>

    <rect class="floor" x="0" y="820" width="1200" height="380" fill="url(#floorTone)"
          role="img" aria-label="Neon magenta perspective grid floor receding to the horizon"/>

    <g class="neon-rails" stroke="var(--neon-line)" stroke-width="4" filter="url(#glow)" opacity="0.9">
      <line x1="0" y1="548" x2="1200" y2="548"/>
      <line x1="0" y1="592" x2="1200" y2="592"/>
      <line x1="0" y1="632" x2="1200" y2="632"/>
      <line x1="0" y1="676" x2="1200" y2="676"/>
    </g>

    <g class="album-title">
      <text x="130" y="678" textLength="976" lengthAdjust="spacingAndGlyphs" fill="var(--extrude-shadow)">VARMEL</text>
      <text x="127" y="675" textLength="976" lengthAdjust="spacingAndGlyphs" fill="var(--extrude-blue)">VARMEL</text>
      <text x="124" y="672" textLength="976" lengthAdjust="spacingAndGlyphs" fill="var(--neon-pink)">VARMEL</text>
    </g>

    <text class="band-name" x="258" y="762" textLength="684" lengthAdjust="spacingAndGlyphs">lanternSOkites</text>
  </svg>
</main>
</body>
</html>
```